Business Card Design

Marla Quibbet
Artist of Contemporary/Modern/Representational Art
Contact: 0457219308
Please include my web site (thanks)! http://www.artvault913.com.au/marla-quibbet
And
Email: marlaquibbet@fernpost.example

Target Market(s)

Modern professional People who know what they like in modern contemporary art and have the means to purchase it.

Industry/Entity Type

Business

Contact Information for Business Card

Marla Quibbet
Contact: 0457219308

Font styles to use
Sans Serif

Requirements
Must have
• Simplicity & to the point
Keep the font modern/ contemporary
Nice to have
• A portrait of me and one piece of work on the business card (one on each side).
Should not have
• I'm not into butterflies.
No feminine style swirls
Nor I like swirls that look like tatoos

```html
<!DOCTYPE html>
<html lang="en">
<head>
<meta charset="utf-8">
<title>Marla Quibbet — Business Card</title>
<link rel="stylesheet" href="https://fonts.googleapis.com/css2?family=Kreon:wght@700&family=Archivo+Black&display=swap">
<style>
  :root {
    --page: #ffffff;
    --card-light: #ffffff;
    --card-mid: #a9aaad;
    --card-dark: #242325;
    --ink-light: #ffffff;
    --sky: #3c5f9a;
    --red: #c8382f;
    --yellow: #e6cf2a;
    --green: #6f9a45;
    --water: #8a5a3e;
  }
  * { margin: 0; padding: 0; box-sizing: border-box; }
  html, body {
    width: 927px;
    height: 1200px;
    overflow: hidden;
    background: var(--page);
  }
  .sheet {
    position: relative;
    width: 927px;
    height: 1200px;
  }
  .card {
    position: absolute;
    left: 27px;
    width: 872px;
    background: linear-gradient(25deg, var(--card-light) 0%, var(--card-mid) 38%, var(--card-dark) 100%);
    color: var(--ink-light);
  }
  .card--front { top: 76px; height: 519px; }
  .card--back { top: 658px; height: 453px; }

  .artwork {
    position: absolute;
    left: 18px;
    top: 16px;
    width: 413px;
    height: 247px;
    background:
      linear-gradient(180deg, var(--sky) 0%, var(--sky) 14%, transparent 14%, transparent 72%, var(--water) 72%),
      linear-gradient(90deg, var(--red) 0%, var(--green) 22%, var(--red) 36%, var(--yellow) 58%, var(--green) 78%, var(--red) 100%);
  }

  .front-text {
    position: absolute;
    right: 55px;
    text-align: right;
    font-family: "Kreon", Georgia, serif;
    font-weight: 700;
    white-space: nowrap;
  }
  .name {
    top: 208px;
    font-size: 50px;
    letter-spacing: 1px;
  }
  .tagline {
    top: 284px;
    font-size: 21px;
  }
  .contact {
    top: 389px;
    font-size: 21px;
    line-height: 31px;
  }

  .back-name {
    position: absolute;
    left: 0;
    right: 0;
    top: 210px;
    padding-left: 34px;
    text-align: center;
    font-family: "Archivo Black", "Arial Black", sans-serif;
    font-size: 62px;
    letter-spacing: 1px;
    color: var(--ink-light);
    white-space: nowrap;
  }
</style>
</head>
<body>
<main class="sheet">
  <section class="card card--front">
    <div class="artwork" role="img" aria-label="Painting of a row of colourful tall townhouses along a waterfront under a blue sky"></div>
    <h1 class="front-text name">Marla Quibbet</h1>
    <p class="front-text tagline">Artist of Contemporary/Modern/Representational Art</p>
    <p class="front-text contact">Contact: 0457219308<br>www.artvault913.com.au/marla-quibbet</p>
  </section>

  <section class="card card--back">
    <p class="back-name">Marla Quibbet</p>
  </section>
</main>
</body>
</html>
```